TOPページのイメージを作成していただきたいです。
女性が入りやすく、親しみやすい色使いとフォントで、
カテゴリのボタンはアイコン等を使い、やわらかい印象を与えたい
※アイコンを指定しているわけではありません。

商品にカラフルなものが多くなりやすいので、全体的な色バランスはシンプルなカラーでお願いします。
サイドバナーとメインに上記スクールをターゲットとしたカテゴリに飛ぶためのバナー用意してほしいです。
近いサイトイメージは合わせて送らせていただきます。
スマートフォンでも表示させやすいレイアウトを希望します。
Quelvoのショッピングに関しては、Quelvoプリズマを契約予定です。
また、今回はトップページだけですが、契約させて頂いた方には商品ページなどサブページも依頼する可能性が高いです

-------------------
項目について
-------------------
※スプレッドシート参照
https://sheets.tavrolink.com/spreadsheets/d/7pxQwLzNc4bTr2VhYk9MeJsA8uDfGiHo3nKyRtE5WqPl/edit?usp=sharing
■ヘッダー
検索窓、お支払いについて、送料、お届けについて、返品、交換、保証について、会社概要、プライバシーポリシー、お問い合わせ、よくある質問
■フッター
店舗内簡易情報として、イメージ画像のような下記の内容を用意する予定で、記述箇所のデザインを用意してください
送料について、支払い方法について、手数料、納期、キャンセルについて、商品の在庫について
■カテゴリ
カテゴリは、別紙の資料の通りです。
大カテゴリがメイン、中に小カテゴリがあります。

■写真資料
https://files.tavrolink.com/file/d/9kd3RwQ7mZ2xVbN8pLcT4yHsJfGeAu6Wn/view?usp=sharing

■サイト見本イメージ
https://store.mirubeta.jp/pastelnook/
https://yarn-lumio.com/
https://ec.stitchvale.jp/
https://www.tomiseki.co.jp/shop/c/c10/
https://www.webshop.mirel-kasano.com/
https://works.brevok.net/
サイトの色合いや雰囲気に近いサイトになります。
1ページ
赤系、黄・オレンジ系、茶系
• イラストレーター形式 (.ai)
幅1250px程度
※Quelvoショップのバナーサイズを考慮しています。
場合によってはその他のページもお願いする可能性があります。
もう少し提案数を頂きたいため、5月13日(金)までコンペの延長をいたします。

今回選ばせていただきました理由は
・商品を邪魔しないシンプルさ
・Quelvoショップに落とし込んだ時に差異が生まれにくい点
・全体的な色使い
を中心に選ばせていただきました。
非常にあたたかく、親しみやすいデザインで作成いただきましたので、こちらに決定させていただきました。

今回いただきました提案はどれも素晴らしく、選考は非常に悩みました。
冒険するか、無難なデザインにするか、また、その中でもどれがいいか、かなり悩みまして、選ばれなかったデザインも、最後までの残ったデザインがいくつかございました。
本当に皆様ご提案ありがとうございました。
また次の機会がございましたら、是非よろしくお願いします。

```html
<!DOCTYPE html>
<html lang="ja">
<head>
<meta charset="utf-8">
<title>Lunafelt 手芸用品のオンラインショップ</title>
<link rel="stylesheet" href="https://fonts.googleapis.com/css2?family=M+PLUS+Rounded+1c:wght@400;500;700&family=Quicksand:wght@500;700&display=swap">
<style>
:root{
  --accent:#d9625c;
  --accent-soft:#f3c9c3;
  --beige:#f5efe8;
  --beige-deep:#ebe2d7;
  --line:#e5ddd3;
  --text:#5a4a42;
  --muted:#9a8c82;
  --blue:#8fb2cf;
  --green:#8ea57a;
  --white:#fff;
}
*{box-sizing:border-box;margin:0;padding:0}
html,body{width:1200px;height:2980px;overflow:hidden}
body{font-family:"M PLUS Rounded 1c",sans-serif;color:var(--text);background:var(--white);position:relative;font-size:12px}
a{color:inherit;text-decoration:none}
.topbar{height:18px;line-height:18px;font-size:10px;color:var(--muted);padding-left:20px}
.header{position:relative;height:122px}
.logo{position:absolute;left:60px;top:22px;display:flex;align-items:center;gap:8px}
.logo-mark{width:14px;height:14px;border-radius:50%;background:var(--accent)}
.logo-name{font-size:30px;font-weight:700;color:var(--accent)}
.logo-sub{position:absolute;left:60px;top:64px;font-size:9px;color:var(--muted);letter-spacing:1px}
.util{position:absolute;right:60px;top:18px;display:flex;gap:16px;font-size:10px;color:var(--muted)}
.search-top{position:absolute;right:60px;top:42px;display:flex;width:300px;height:32px}
.search-top input{flex:1;border:1px solid var(--line);border-right:none;border-radius:4px 0 0 4px;padding:0 10px;font:inherit;font-size:11px;color:var(--muted)}
.search-btn{width:34px;background:var(--accent);border-radius:0 4px 4px 0;display:flex;align-items:center;justify-content:center}
.gnav{position:absolute;left:360px;top:84px;display:flex;gap:36px}
.gnav a{display:flex;align-items:center;gap:8px;font-size:13px;font-weight:500}
.gnav-icon{width:30px;height:30px;border-radius:50%;background:var(--beige);display:flex;align-items:center;justify-content:center}

.hero{position:relative;height:600px;background:var(--beige)}
.slide-side{position:absolute;top:20px;height:530px}
.slide-prev{left:0;width:130px;background:#ddd5cc}
.slide-next{right:0;width:170px;background:#f1c6b6;padding:60px 0 0 20px;color:var(--white)}
.slide-next .big{font-family:"Quicksand",sans-serif;font-size:60px;font-weight:700;line-height:1.05}
.slide-next .date{display:inline-block;margin-top:20px;background:var(--white);color:var(--accent);font-weight:700;font-size:22px;padding:4px 10px}
.slide-main{position:absolute;left:150px;top:20px;width:860px;height:530px;background:#efe6d8;overflow:hidden}
.slide-photo{position:absolute;border-radius:50%}
.slide-band{position:absolute;left:0;right:0;bottom:70px;height:90px;background:var(--green);display:flex;align-items:center;justify-content:center;gap:24px;color:var(--white)}
.slide-band .badge{width:84px;height:84px;border-radius:50%;background:var(--accent);display:flex;align-items:center;justify-content:center;text-align:center;font-weight:700;font-size:17px;line-height:1.2;margin-top:-30px}
.slide-band .title{font-size:38px;font-weight:700;letter-spacing:2px}
.slide-band .when{font-size:10px;line-height:1.6}
.dots{position:absolute;left:0;right:0;bottom:22px;display:flex;justify-content:center;gap:10px}
.dots span{width:9px;height:9px;border-radius:50%;background:#d6ccc1}
.dots span.on{background:var(--accent)}

.sidebar{position:absolute;left:70px;top:760px;width:230px}
.side-banner{height:100px;background:#efe6d8;border-radius:4px;position:relative;overflow:hidden}
.side-banner .img{position:absolute;left:0;top:0;width:90px;height:100px;background:#d9c7b2}
.side-banner .txt{position:absolute;left:100px;top:22px;font-weight:700;font-size:14px;color:var(--accent);line-height:1.5}
.side-ship{margin-top:18px;height:60px;background:var(--blue);border-radius:4px;color:var(--white);display:flex;align-items:center;gap:10px;padding-left:16px;font-size:12px;font-weight:700;line-height:1.4}
.side-label{margin-top:24px;font-size:12px;font-weight:700;display:flex;align-items:center;gap:6px}
.side-label i{width:16px;height:16px;border-radius:50%;background:var(--accent);display:inline-block}
.side-search{margin-top:10px;display:flex;height:34px}
.side-search input{flex:1;border:1px solid var(--line);border-right:none;border-radius:4px 0 0 4px;padding:0 10px;font:inherit;font-size:11px;color:var(--muted)}
.cat-list{list-style:none;margin-top:10px;border-top:1px solid var(--line)}
.cat-list li{height:48px;border-bottom:1px solid var(--line);display:flex;align-items:center;gap:12px;padding:0 6px;font-size:12px}
.cat-list li .ic{width:18px;height:18px;border-radius:50%;background:var(--beige-deep);flex:none}
.cat-list li .arr{margin-left:auto;color:var(--muted)}
.side-cal{margin-top:50px}

.cal-title{font-size:12px;font-weight:700;padding-bottom:8px;border-bottom:2px solid var(--accent)}
.cal-month{text-align:center;font-size:11px;margin:10px 0 6px}
.cal{width:100%;border-collapse:collapse;font-size:10px;text-align:center}
.cal th,.cal td{border:1px solid var(--line);height:24px}
.cal th{background:var(--beige);font-weight:500}
.cal td.off{background:var(--accent);color:var(--white)}
.cal-note{margin-top:8px;font-size:10px;display:flex;align-items:center;gap:6px}
.cal-note i{width:12px;height:12px;background:var(--accent);display:inline-block}

.main{position:absolute;left:350px;top:720px;width:790px}
.section{border:1px solid var(--line);border-radius:4px;padding:0 24px 28px;margin-bottom:22px}
.section-head{height:54px;display:flex;align-items:center;gap:10px;font-size:16px;font-weight:700;border-bottom:1px solid var(--line);margin:0 -24px 24px;padding:0 24px}
.section-head i{width:22px;height:22px;border-radius:50%;background:var(--accent-soft);display:inline-block}
.grid{display:grid;grid-template-columns:repeat(4,1fr);gap:30px 26px}
.item-img{height:150px;border-radius:2px}
.tag{display:inline-block;margin-top:8px;background:var(--accent);color:var(--white);font-size:9px;padding:2px 6px;border-radius:2px}
.item-name{margin-top:6px;font-size:11px;line-height:1.5;height:34px;overflow:hidden}
.item-price{margin-top:8px;text-align:right;font-size:13px;font-weight:700}
.item-price small{font-size:9px;font-weight:400}

.news-item{display:flex;gap:18px;padding:14px 0;border-bottom:1px dashed var(--line)}
.news-thumb{width:90px;height:76px;flex:none}
.news-meta{font-size:10px;color:var(--muted);display:flex;gap:8px;align-items:center}
.news-meta span{background:var(--beige-deep);color:var(--text);padding:1px 6px;border-radius:2px}
.news-title{margin-top:8px;font-size:12px;font-weight:500;color:var(--accent)}

.footer{position:absolute;left:0;top:2510px;width:1200px;height:430px;background:var(--beige);padding:36px 60px 0;display:flex;gap:50px}
.f-col{width:235px}
.f-head{font-size:13px;font-weight:700;padding-bottom:8px;border-bottom:1px solid var(--beige-deep);margin-bottom:12px}
.f-shop{display:flex;gap:12px}
.f-photo{width:110px;height:80px;background:#bfae98;flex:none}
.f-addr{font-size:10px;line-height:1.6}
.f-links{list-style:none}
.f-links li{font-size:11px;height:28px;display:flex;align-items:center;gap:8px}
.f-links li::before{content:"";width:6px;height:6px;border-radius:50%;background:var(--accent)}
.copy{position:absolute;left:0;top:2940px;width:1200px;height:40px;background:var(--accent-soft);text-align:center;line-height:40px;font-size:10px}
</style>
</head>
<body>
<div class="topbar">手芸用品のオンラインショップ Lunafelt｜親子で楽しめる材料をお届け</div>
<header class="header">
  <a class="logo" href="#"><span class="logo-mark"></span><span class="logo-name">Lunafelt</span></a>
  <div class="logo-sub">HANDMADE SUPPLY SHOP</div>
  <nav class="util"><a href="#">会社概要</a><a href="#">プライバシーポリシー</a><a href="#">お問い合わせ</a><a href="#">返品・交換・保証</a></nav>
  <form class="search-top"><input value="キーワードを入力"><span class="search-btn"><svg width="14" height="14" viewBox="0 0 14 14"><circle cx="6" cy="6" r="4.5" fill="none" stroke="#fff" stroke-width="1.6"/><line x1="9.5" y1="9.5" x2="13" y2="13" stroke="#fff" stroke-width="1.6"/></svg></span></form>
  <nav class="gnav">
    <a href="#"><span class="gnav-icon"><svg width="16" height="16" viewBox="0 0 16 16"><rect x="2" y="5" width="12" height="9" rx="1" fill="none" stroke="#d9625c" stroke-width="1.4"/><path d="M5 5V3.5a3 3 0 0 1 6 0V5" fill="none" stroke="#d9625c" stroke-width="1.4"/></svg></span>各種商品</a>
    <a href="#"><span class="gnav-icon"><svg width="18" height="14" viewBox="0 0 18 14"><rect x="1" y="2" width="10" height="8" fill="none" stroke="#d9625c" stroke-width="1.4"/><path d="M11 5h4l2 3v2h-6" fill="none" stroke="#d9625c" stroke-width="1.4"/><circle cx="5" cy="12" r="1.5" fill="#d9625c"/><circle cx="14" cy="12" r="1.5" fill="#d9625c"/></svg></span>送料・お届け方法</a>
    <a href="#"><span class="gnav-icon"><svg width="16" height="16" viewBox="0 0 16 16"><circle cx="8" cy="8" r="6.5" fill="none" stroke="#d9625c" stroke-width="1.4"/><text x="8" y="11.5" font-size="9" text-anchor="middle" fill="#d9625c">?</text></svg></span>よくある質問</a>
    <a href="#"><span class="gnav-icon"><svg width="16" height="14" viewBox="0 0 16 14"><rect x="1" y="2" width="14" height="10" rx="1" fill="none" stroke="#d9625c" stroke-width="1.4"/><path d="M1.5 2.5 8 8l6.5-5.5" fill="none" stroke="#d9625c" stroke-width="1.4"/></svg></span>お問い合わせ</a>
  </nav>
</header>

<section class="hero">
  <div class="slide-side slide-prev" role="img" aria-label="前のバナー画像"></div>
  <div class="slide-main">
    <div class="slide-photo" role="img" aria-label="工作をする親子の写真" style="left:150px;top:40px;width:250px;height:250px;background:#d8c4ae"></div>
    <div class="slide-photo" role="img" aria-label="手作りの作品と道具の写真" style="left:460px;top:30px;width:230px;height:230px;background:#cbb9a5"></div>
    <div class="slide-band">
      <div class="badge">親子で<br>楽しむ</div>
      <div class="title">イベントワークショップ</div>
      <div class="when">2022/05/01<br>〜2022/05/31</div>
    </div>
  </div>
  <div class="slide-side slide-next"><div class="big">Lorem<br>Ipsum</div><div class="date">2022/05</div></div>
  <div class="dots"><span class="on"></span><span></span><span></span><span></span></div>
</section>

<aside class="sidebar">
  <a class="side-banner" href="#" style="display:block"><span class="img" role="img" aria-label="ワークショップの写真"></span><span class="txt">親子で楽しむ<br>イベント<br>ワークショップ</span></a>
  <a class="side-ship" href="#"><svg width="26" height="20" viewBox="0 0 18 14"><rect x="1" y="2" width="10" height="8" fill="none" stroke="#fff" stroke-width="1.4"/><path d="M11 5h4l2 3v2h-6" fill="none" stroke="#fff" stroke-width="1.4"/><circle cx="5" cy="12" r="1.5" fill="#fff"/><circle cx="14" cy="12" r="1.5" fill="#fff"/></svg><span>送料・お届け方法<br>について</span></a>
  <div class="side-label"><i></i>キーワードから探す</div>
  <form class="side-search"><input value="キーワードを入力"><span class="search-btn"><svg width="14" height="14" viewBox="0 0 14 14"><circle cx="6" cy="6" r="4.5" fill="none" stroke="#fff" stroke-width="1.6"/><line x1="9.5" y1="9.5" x2="13" y2="13" stroke="#fff" stroke-width="1.6"/></svg></span></form>
  <div class="side-label"><i></i>カテゴリから探す</div>
  <ul class="cat-list">
    <li><span class="ic"></span>新着商品<span class="arr">›</span></li>
    <li><span class="ic"></span>画材・ペーパークラフト<span class="arr">›</span></li>
    <li><span class="ic"></span>加工素材<span class="arr">›</span></li>
    <li><span class="ic"></span>事務用品<span class="arr">›</span></li>
    <li><span class="ic"></span>加工道具<span class="arr">›</span></li>
    <li><span class="ic"></span>カット素材<span class="arr">›</span></li>
    <li><span class="ic"></span>紙工材<span class="arr">›</span></li>
    <li><span class="ic"></span>布地<span class="arr">›</span></li>
    <li><span class="ic"></span>リボン・紐<span class="arr">›</span></li>
    <li><span class="ic"></span>バッグ製品<span class="arr">›</span></li>
    <li><span class="ic"></span>アイロンシート用品<span class="arr">›</span></li>
    <li><span class="ic"></span>イベントセット<span class="arr">›</span></li>
    <li><span class="ic"></span>スタートキット<span class="arr">›</span></li>
  </ul>
  <div class="side-cal">
    <div class="cal-title">営業日カレンダー</div>
    <div class="cal-month">2022年5月</div>
    <table class="cal">
      <tr><th>日</th><th>月</th><th>火</th><th>水</th><th>木</th><th>金</th><th>土</th></tr>
      <tr><td class="off">1</td><td>2</td><td class="off">3</td><td class="off">4</td><td class="off">5</td><td>6</td><td class="off">7</td></tr>
      <tr><td class="off">8</td><td>9</td><td>10</td><td>11</td><td>12</td><td>13</td><td class="off">14</td></tr>
      <tr><td class="off">15</td><td>16</td><td>17</td><td>18</td><td>19</td><td>20</td><td class="off">21</td></tr>
      <tr><td class="off">22</td><td>23</td><td>24</td><td>25</td><td>26</td><td>27</td><td class="off">28</td></tr>
      <tr><td class="off">29</td><td>30</td><td>31</td><td></td><td></td><td></td><td></td></tr>
    </table>
    <div class="cal-note"><i></i>休業日</div>
  </div>
</aside>

<main class="main">
  <section class="section">
    <h2 class="section-head"><i></i>おすすめアイテム</h2>
    <div class="grid">
      <div><div class="item-img" role="img" aria-label="カッティングマシンの商品写真" style="background:#e4e4e6"></div><span class="tag">おすすめ</span><p class="item-name">刺繍用カッティングマシン 厚紙にも対応 本体セット</p><p class="item-price">7,780円<small>(税込)</small></p></div>
      <div><div class="item-img" role="img" aria-label="カッターナイフの商品写真" style="background:#f0ead8"></div><span class="tag">おすすめ</span><p class="item-name">クラフト用カッター 替刃付き 細工向け</p><p class="item-price">3,300円<small>(税込)</small></p></div>
      <div><div class="item-img" role="img" aria-label="カッティングマットの商品写真" style="background:#8d8f92"></div><span class="tag">おすすめ</span><p class="item-name">大判カッティングマット 方眼入り A2サイズ</p><p class="item-price">9,900円<small>(税込)</small></p></div>
      <div><div class="item-img" role="img" aria-label="布素材の商品写真" style="background:#d4c7b6"></div><span class="tag">おすすめ</span><p class="item-name">綿素材 手染め用 布地セット 3枚入り</p><p class="item-price">11,000円<small>(税込)</small></p></div>
      <div><div class="item-img" role="img" aria-label="白い用紙の商品写真" style="background:#eeeeee"></div><span class="tag">おすすめ</span><p class="item-name">転写用シート 白 A4 10枚入り</p><p class="item-price">260円<small>(税込)</small></p></div>
      <div><div class="item-img" role="img" aria-label="カラーサンプル帳の商品写真" style="background:#c9b8d8"></div><span class="tag">おすすめ</span><p class="item-name">アイロンシート カラー見本帳 全色セット</p><p class="item-price">5,250円<small>(税込)</small></p></div>
      <div><div class="item-img" role="img" aria-label="カラーシートの商品写真" style="background:#5d6a86"></div><span class="tag">おすすめ</span><p class="item-name">カラーシート 8色アソート A4サイズ</p><p class="item-price">9,900円<small>(税込)</small></p></div>
      <div><div class="item-img" role="img" aria-label="トートバッグの商品写真" style="background:#e2d2b8"></div><span class="tag">おすすめ</span><p class="item-name">無地キャンバストートバッグ ナチュラル</p><p class="item-price">11,000円<small>(税込)</small></p></div>
    </div>
  </section>

  <section class="section">
    <h2 class="section-head"><i></i>新着アイテム</h2>
    <div class="grid">
      <div><div class="item-img" role="img" aria-label="トートバッグの商品写真" style="background:#e2d2b8"></div><span class="tag">新着</span><p class="item-name">無地キャンバストートバッグ ナチュラル</p><p class="item-price">7,780円<small>(税込)</small></p></div>
      <div><div class="item-img" role="img" aria-label="カラーペンセットの商品写真" style="background:#d9c7cf"></div><span class="tag">新着</span><p class="item-name">布用カラーペン 12色セット 洗濯対応</p><p class="item-price">3,300円<small>(税込)</small></p></div>
      <div><div class="item-img" role="img" aria-label="カッティングマシンの商品写真" style="background:#e4e4e6"></div><span class="tag">新着</span><p class="item-name">小型カッティングマシン 家庭用モデル</p><p class="item-price">9,900円<small>(税込)</small></p></div>
      <div><div class="item-img" role="img" aria-label="プレス機の商品写真" style="background:#d8d8d8"></div><span class="tag">新着</span><p class="item-name">卓上アイロンプレス機 小型タイプ</p><p class="item-price">11,000円<small>(税込)</small></p></div>
    </div>
  </section>

  <section class="section">
    <h2 class="section-head"><i></i>お知らせ</h2>
    <div class="news-item"><div class="news-thumb" role="img" aria-label="ワークショップの写真" style="background:#d8c4ae"></div><div><p class="news-meta">2022.05.01<span>イベント</span></p><p class="news-title">【イベント】親子ワークショップ開催のお知らせ 5月の参加者を募集中です</p></div></div>
    <div class="news-item"><div class="news-thumb" role="img" aria-label="作品の写真" style="background:#e3d6c6"></div><div><p class="news-meta">2022.04.28<span>お知らせ</span></p><p class="news-title">【新商品】布用カラーペンの取り扱いを開始しました</p></div></div>
    <div class="news-item"><div class="news-thumb" role="img" aria-label="店舗の写真" style="background:#cfc3b4"></div><div><p class="news-meta">2022.04.20<span>お知らせ</span></p><p class="news-title">【営業日】大型連休中の発送スケジュールについて</p></div></div>
    <div class="news-item"><div class="news-thumb" role="img" aria-label="材料の写真" style="background:#bfae98"></div><div><p class="news-meta">2022.04.10<span>イベント</span></p><p class="news-title">【キャンペーン】春の手作り応援セールを開催いたします</p></div></div>
  </section>
</main>

<footer class="footer">
  <div class="f-col" style="width:300px">
    <div class="f-head">店舗情報</div>
    <div class="f-shop"><div class="f-photo" role="img" aria-label="店舗内の写真"></div><p class="f-addr">Lunafelt<br>営業時間 10:00〜17:00<br>定休日 土日祝</p></div>
    <div class="cal-month">2022年5月</div>
    <table class="cal">
      <tr><th>日</th><th>月</th><th>火</th><th>水</th><th>木</th><th>金</th><th>土</th></tr>
      <tr><td class="off">1</td><td>2</td><td class="off">3</td><td class="off">4</td><td class="off">5</td><td>6</td><td class="off">7</td></tr>
      <tr><td class="off">8</td><td>9</td><td>10</td><td>11</td><td>12</td><td>13</td><td class="off">14</td></tr>
      <tr><td class="off">15</td><td>16</td><td>17</td><td>18</td><td>19</td><td>20</td><td class="off">21</td></tr>
      <tr><td class="off">22</td><td>23</td><td>24</td><td>25</td><td>26</td><td>27</td><td class="off">28</td></tr>
      <tr><td class="off">29</td><td>30</td><td>31</td><td></td><td></td><td></td><td></td></tr>
    </table>
    <div class="cal-note"><i></i>休業日</div>
  </div>
  <div class="f-col">
    <div class="f-head">お買い物ガイド</div>
    <ul class="f-links"><li>送料について</li><li>支払い方法について</li><li>手数料について</li><li>納期について</li><li>キャンセルについて</li><li>商品の在庫について</li></ul>
  </div>
  <div class="f-col">
    <div class="f-head">よくある質問</div>
    <ul class="f-links"><li>お届けについて</li><li>返品・交換について</li><li>保証について</li></ul>
  </div>
  <div class="f-col">
    <div class="f-head">お問い合わせ</div>
    <ul class="f-links"><li>会社概要</li><li>プライバシーポリシー</li><li>お問い合わせフォーム</li></ul>
  </div>
</footer>
<div class="copy">Copyright © Lunafelt All Rights Reserved.</div>
</body>
</html>
```